BRAVELUX Program Cover

Every year, we host an annual conference for educators who teach in afterschool in the Southwest. This year, we are renaming the conference to BRAVELUX 2014 (stands for Beyond-Bell-Hours Learning Summit). The theme of our conference is made up of three verbs: Innovate, Collaborate, & Thrive. We are looking for a program cover that is creative and yet visually appealing to an audience that ranges from Millennials to Baby Boomers. It needs to convey the three verbs and also brand the conference with the new name. We like the colors Blue and Green as our previous programs have been red, gold, yellow, and orange. Our audience teaches kids from K - 12, but likes to be treated as professionals (not the typical school clipart stuff). The conference is hosted at the Ft. Worth Calloway Lodge from July 23rd to July 24th, 2014. The program cover will set the tone for all conference materials (i.e. color scene, potential logo, etc...).

Target Market(s)

The target audience is participants of the conference. The age ranges from 25 to 60, but they are all either teachers, social workers, or educational administrators. All have a Bachelor's Degree or higher. While they are professionals, they also like to have fun.

Industry/Entity Type

Graphic Design

Requirements
Must have
• BRAVELUX must be prevalent and tagged with Beyond-Bell-Hours Learning Summit so that people know what it stands for.
Should not have
• The design should be clean with zero clipart.

```html
<!DOCTYPE html>
<html lang="en">
<head>
<meta charset="utf-8">
<title>BRAVELUX Program Cover</title>
<link rel="stylesheet" href="https://fonts.googleapis.com/css2?family=Oswald:wght@400;700&family=Tinos&family=Lato:wght@900&display=swap">
<style>
  :root {
    --page-bg: #e9ece8;
    --navy-deep: #14184f;
    --navy: #1b2466;
    --glow: #1fa6e6;
    --glow-mid: #1565b4;
    --line-cyan: #3fb4ee;
    --year-blue: #93a9e4;
    --tagline: rgba(140, 168, 214, 0.55);
    --white: #ffffff;
  }
  * { margin: 0; padding: 0; box-sizing: border-box; }
  html, body {
    width: 1200px; height: 1129px; overflow: hidden;
    background: var(--page-bg);
  }
  .cover {
    position: absolute; left: 243px; top: 60px;
    width: 713px; height: 1009px; overflow: hidden;
    background: radial-gradient(circle at 46% 46%, var(--glow) 0%, var(--glow-mid) 28%, var(--navy) 58%, var(--navy-deep) 100%);
    box-shadow: 0 6px 18px rgba(0,0,0,0.25);
  }
  .header-band {
    position: absolute; left: 0; top: 0; width: 100%; height: 300px;
    background: linear-gradient(180deg, var(--navy-deep) 0%, rgba(27,36,102,0.85) 70%, rgba(27,36,102,0) 100%);
  }
  .footer-band {
    position: absolute; left: 0; bottom: 0; width: 100%; height: 140px;
    background: linear-gradient(0deg, var(--navy-deep) 0%, rgba(20,24,79,0.9) 60%, rgba(20,24,79,0) 100%);
  }
  .decor-binary {
    position: absolute; left: 0; top: 300px; width: 320px; height: 620px;
    background: linear-gradient(180deg, rgba(90,130,200,0.12), rgba(90,130,200,0.05));
  }
  .decor-waves-top {
    position: absolute; left: 420px; top: 190px; width: 260px; height: 200px;
    background: radial-gradient(ellipse at 50% 50%, rgba(110,150,220,0.22), rgba(110,150,220,0) 70%);
  }
  .decor-waves-bottom {
    position: absolute; left: 330px; top: 680px; width: 383px; height: 250px;
    background: radial-gradient(ellipse at 70% 60%, rgba(110,150,220,0.22), rgba(110,150,220,0) 70%);
  }
  .rules { position: absolute; left: 0; top: 0; }
  .event-name {
    position: absolute; left: 100px; top: 140px;
    font: 700 86px/1 "Oswald", sans-serif; color: var(--white);
    letter-spacing: 1px;
  }
  .event-year {
    position: absolute; left: 462px; top: 62px;
    font: 700 88px/1 "Oswald", sans-serif; color: var(--year-blue);
  }
  .event-tagline {
    position: absolute; left: 104px; top: 262px;
    font: 400 19px/1 "Oswald", sans-serif; color: var(--white);
  }
  .theme {
    position: absolute; left: 0; top: 0;
    font: 400 46px/1 "Tinos", serif; color: var(--tagline);
    white-space: nowrap;
  }
  .theme-innovate { left: 440px; top: 385px; }
  .theme-collaborate { left: 320px; top: 428px; }
  .theme-thrive { left: 480px; top: 471px; }
  .venue {
    position: absolute; left: 405px; top: 850px;
    font: 900 19px/1.35 "Lato", sans-serif; color: var(--white);
  }
</style>
</head>
<body>
  <main class="cover">
    <div class="header-band"></div>
    <div class="decor-binary" role="img" aria-label="Faint binary digit texture"></div>
    <div class="decor-waves-top" role="img" aria-label="Fine flowing wire-mesh waves"></div>
    <div class="decor-waves-bottom" role="img" aria-label="Fine flowing wire-mesh waves"></div>
    <div class="footer-band"></div>

    <svg class="rules" width="713" height="1009" viewBox="0 0 713 1009" aria-hidden="true">
      <path d="M0 298 H390 Q398 298 400 290 L404 252 Q406 244 414 244 H713" fill="none" stroke="var(--line-cyan)" stroke-width="2"/>
      <path d="M713 900 H392 Q384 900 382 908 L379 930 Q377 938 369 938 H0" fill="none" stroke="var(--line-cyan)" stroke-width="2"/>
    </svg>

    <div class="event-year">2014</div>
    <h1 class="event-name">BRAVELUX</h1>
    <p class="event-tagline">Beyond-Bell-Hours Learning Summit</p>

    <p class="theme theme-innovate">Innovate,</p>
    <p class="theme theme-collaborate">Collaborate &amp;</p>
    <p class="theme theme-thrive">Thrive.</p>

    <p class="venue">Ft. Worth Calloway Lodge<br>July 23rd to July 24th, 2014.</p>
  </main>
</body>
</html>
```